Lundor Vapor Cleaning website for demos

Lundor Vapor Cleaning is a business that provides commercial cleaning services utilizing steam vapor, which offers the most effective and ecologically friendly method of cleaning today. We need a website to advertise our services, and needs to incorporate spaces to show video demonstrations on how the cleaning machine works.

Target Market(s)

The potential market for this business are hotels, motels, restaurants, hospitals, fast food facilities, nursing homes, day care centers, schools, country clubs, churches, office and apartment buildings, malls, movie theaters, super markets, airports, parks, and any other facility.

Industry/Entity Type

Business

Coding

Coded - Design and coding required

Number of Pages Required

3 page

Colors
add136
9bcb3c
34a6d7
3176b5
edf8f6

Requirements
Must have
• Areas for videos that serve as demonstrations of our services

```html
<!DOCTYPE html>
<html lang="en">
<head>
<meta charset="utf-8">
<title>About Us – Lundor Vapor Cleaning</title>
<link href="https://fonts.googleapis.com/css2?family=Arimo:wght@400;700&family=Tinos&display=swap" rel="stylesheet">
<style>
  :root {
    --page-bg: #c4eaf8;
    --header-top: #1ec8f8;
    --header-bottom: #d6f4fc;
    --nav-bg: #34a6d7;
    --content-bg: #edf8f6;
    --footer-top: #d4f2fb;
    --footer-bottom: #3aa9d9;
    --brand: #3176b5;
    --brand-dot: #9bcb3c;
    --nav-text: #1b3646;
    --body-text: #3d4447;
    --frame: #f4fbfe;
  }
  * { margin: 0; padding: 0; box-sizing: border-box; }
  html, body {
    width: 1200px; height: 588px; overflow: hidden;
    background: var(--page-bg);
    font-family: "Arimo", Arial, sans-serif;
  }
  .site {
    position: absolute; left: 19px; top: 28px;
    width: 1149px; height: 323px;
    border: 1.5px solid var(--frame);
    border-radius: 11px; overflow: hidden;
  }
  .site-header {
    height: 94px;
    background: linear-gradient(to bottom, var(--header-top), var(--header-bottom));
    position: relative;
  }
  .brand {
    position: absolute; left: 24px; top: 24px;
    display: flex; align-items: center; gap: 12px;
  }
  .brand-dot {
    width: 64px; height: 64px; border-radius: 50%;
    background: var(--brand-dot);
  }
  .brand-name {
    font-size: 22px; font-weight: 700; color: var(--brand);
  }
  .main-nav {
    height: 34px; background: var(--nav-bg);
    display: flex; align-items: center;
  }
  .main-nav a {
    position: absolute;
    font-family: "Tinos", "Times New Roman", serif;
    font-size: 13.5px; color: var(--nav-text); text-decoration: none;
  }
  .main-nav { position: relative; }
  .nav-home { left: 23px; }
  .nav-demos { left: 91px; }
  .nav-about { left: 213px; }
  .nav-contact { left: 298px; }
  .content {
    height: 125px; background: var(--content-bg);
    padding: 22px 18px 0 18px; color: var(--body-text);
  }
  .content h1 {
    font-size: 19.5px; font-weight: 700; line-height: 1; margin-bottom: 12px;
  }
  .content p {
    font-size: 11px; line-height: 13.3px; margin-bottom: 11px;
  }
  .footer-band { height: 14px; background: var(--nav-bg); }
  .site-footer {
    height: 56px;
    background: linear-gradient(to bottom, var(--footer-top), var(--footer-bottom));
    padding: 23px 0 0 23px;
    font-size: 11px; color: var(--nav-text);
  }
</style>
</head>
<body>
  <div class="site">
    <header class="site-header">
      <div class="brand">
        <span class="brand-dot"></span>
        <span class="brand-name">Lundor Vapor Cleaning</span>
      </div>
    </header>
    <nav class="main-nav">
      <a class="nav-home" href="#">Home</a>
      <a class="nav-demos" href="#">Demonstrations</a>
      <a class="nav-about" href="#">About us</a>
      <a class="nav-contact" href="#">Contact Us</a>
    </nav>
    <main class="content">
      <h1>About Us</h1>
      <p>Lundor Vapor Cleaning is a business that provides commercial cleaning services utilizing steam vapor, which offers the most effective and ecologically friendly method of cleaning today.</p>
      <p>The potential market for this business are hotels, motels, restaurants, hospitals, fast food facilities, nursing homes, day care centers, schools, country clubs, churches, office and apartment buildings, malls, movie theaters, super markets, airports, parks, and any other facility.</p>
    </main>
    <div class="footer-band"></div>
    <footer class="site-footer">&copy;</footer>
  </div>
</body>
</html>
```